VELMARA IMAGING
Ultrasound Imaging Services
VELMARA IMAGING - Imaging
Creative Brief
Professional
Dorvan Tessliff
Ultrasound Diagnostic
5873 Calloway ridge ln Raleigh, NC 27614
dorvantessliff@mailvane.net
Concepts
Logo for mobile ultrasound

```html
<!DOCTYPE html>
<html lang="en">
<head>
<meta charset="utf-8">
<title>Dorvan Tessliff – Ultrasound Diagnostic</title>
<link href="https://fonts.googleapis.com/css2?family=Open+Sans:wght@600;700&display=swap" rel="stylesheet">
<style>
  :root {
    --card-blue: #3f73c9;
    --wave-white: #ffffff;
    --ink-navy: #14136b;
    --rule-light: #8fb0e6;
    --mark-white: #e9f0fb;
  }
  html, body {
    margin: 0;
    padding: 0;
    width: 1200px;
    height: 682px;
    overflow: hidden;
    background: var(--wave-white);
  }
  .business-card {
    position: relative;
    width: 1200px;
    height: 682px;
    background: var(--card-blue);
    font-family: "Open Sans", Verdana, sans-serif;
    color: var(--ink-navy);
    overflow: hidden;
  }
  .card-shapes {
    position: absolute;
    inset: 0;
  }
  .holder-name {
    position: absolute;
    left: 115px;
    top: 140px;
    margin: 0;
    font-size: 43px;
    font-weight: 700;
    letter-spacing: 0.5px;
  }
  .holder-role {
    position: absolute;
    left: 115px;
    top: 214px;
    margin: 0;
    font-size: 39px;
    font-weight: 700;
  }
  .postal-address {
    position: absolute;
    left: 350px;
    top: 382px;
    margin: 0;
    font-style: normal;
    font-size: 35px;
    font-weight: 700;
    line-height: 50px;
  }
  .contact-divider {
    position: absolute;
    left: 790px;
    top: 384px;
    width: 3px;
    height: 94px;
    background: var(--ink-navy);
  }
  .phone-list {
    position: absolute;
    left: 816px;
    top: 382px;
    margin: 0;
    font-size: 35px;
    font-weight: 700;
    line-height: 50px;
  }
  .email-address {
    position: absolute;
    right: 72px;
    top: 555px;
    margin: 0;
    font-size: 36px;
    font-weight: 700;
  }
  .brand-mark {
    position: absolute;
    left: 44px;
    top: 470px;
    display: flex;
    align-items: center;
    gap: 14px;
    color: var(--mark-white);
    font-size: 30px;
    font-weight: 700;
    letter-spacing: 1px;
  }
  .brand-dot {
    width: 26px;
    height: 26px;
    border-radius: 50%;
    background: var(--mark-white);
  }
</style>
</head>
<body>
  <main class="business-card">
    <svg class="card-shapes" width="1200" height="682" viewBox="0 0 1200 682" aria-hidden="true">
      <path class="top-wave" d="M430 0 C 560 70 640 110 760 110 C 900 110 980 170 1080 240 C 1130 275 1170 300 1200 312 L1200 0 Z" fill="var(--wave-white)"/>
      <line class="bottom-rule" x1="0" y1="619" x2="1200" y2="619" stroke="var(--rule-light)" stroke-width="2"/>
    </svg>

    <h1 class="holder-name">Dorvan Tessliff</h1>
    <p class="holder-role">Ultrasound Diagnostic</p>

    <address class="postal-address">5873 Calloway ridge<br>ln Raleigh, NC 27614</address>
    <div class="contact-divider"></div>
    <p class="phone-list">T 919 555 0142<br>C 919-555-0187</p>

    <p class="email-address">dorvantessliff@mailvane.net</p>

    <div class="brand-mark">
      <span class="brand-dot"></span>
      <span class="brand-name">VELMARA</span>
    </div>
  </main>
</body>
</html>
```